Need Plexora Ads for Tyre Company

Need some plexora ads graphics for our tyre company Tyre Ferns that only operates in the cayman islands.

Need Ratio Ads: 1000x1000, 1910x1000, 300x600

Important things to have the customer know:
-Email : info@tyreferns.example
-Phone: +1 345 555 0142
-Address: 41 Marlow Lane, George Town, Cayman Islands
-Website: tyreferns.example (Please see our website for the tyres we offer)
- Common Car brands that our Tyres are compatible with: Kelvar, Pratova, Zolt Quira, Bexmont, Tavel, Lorimo, Feravi, Drastelmor
- Our tyres are priced from KYD$55-$60
-We offer free installation on tyres when customers come to our facility to get them changed.
-We sell tyres in bulk and individually.

*You can choose which things to add or omit for the best look, feel free to reword any of the above also to better fit in.
*Please keep in mind that these will have to be viewed in small formats aswell since they are for plexora ads. Please ensure everything is readable when zoomed out.

Target Market(s)

car rental companies & individuals who need to get their tyres replace

Industry/Entity Type

Automotive, Tyre replacement, Car Parts

Colors
EB3D1F
EC4F4E
F09395
F8D3D4
FCEDEE

Requirements
Must have
• Phone, Location, Brands that our tyres are compatible with, Same theme as our logo(Red & Black, White), design adapted to the 3 ratios listed above
Nice to have
• Creative advertising

```html
<!DOCTYPE html>
<html lang="en">
<head>
<meta charset="utf-8">
<title>Tyre Ferns – Square Ad</title>
<link rel="stylesheet" href="https://fonts.googleapis.com/css2?family=Saira:ital,wght@0,500;0,600;0,700;1,800&family=Arimo:wght@400&display=swap">
<style>
  :root {
    --red: #eb3d1f;
    --red-soft: #ec4f4e;
    --ink: #1f1f1f;
    --panel: #242424;
    --panel-deep: #1a1a1a;
    --white: #ffffff;
    --stage: #ececec;
    --grey: #bdbdbd;
  }
  * { box-sizing: border-box; margin: 0; padding: 0; }
  html, body { width: 1200px; height: 1036px; overflow: hidden; background: var(--stage); }
  .ad {
    position: absolute; left: 120px; top: 38px;
    width: 960px; height: 960px;
    background: var(--panel);
    font-family: "Saira", sans-serif;
    color: var(--white);
    overflow: hidden;
  }
  .ad-header {
    height: 202px; background: var(--white);
    display: flex; align-items: center; justify-content: center; gap: 18px;
  }
  .brand-mark { width: 56px; height: 56px; border-radius: 50%; background: var(--ink); }
  .brand-name { font-size: 64px; font-weight: 700; color: var(--ink); letter-spacing: 1px; }
  .ad-body {
    position: absolute; top: 202px; left: 0; right: 0; height: 643px;
    background: radial-gradient(ellipse at 40% 40%, #2c2c2c 0%, var(--panel-deep) 80%);
  }
  .price-lead {
    position: absolute; left: 62px; top: 78px;
    font-size: 24px; font-weight: 700; letter-spacing: 1.5px; text-transform: uppercase;
  }
  .price-lead .accent { color: var(--red); }
  .price {
    position: absolute; left: 60px; top: 118px;
    font-size: 74px; font-weight: 800; font-style: italic; line-height: 1;
    white-space: nowrap;
  }
  .price .amount { color: var(--red); }
  .price .dollar { font-size: 40px; vertical-align: 22px; margin: 0 4px 0 14px; }
  .price .dash { font-size: 50px; margin-left: 10px; vertical-align: 8px; }
  .install-note {
    position: absolute; left: 72px; top: 270px; width: 470px;
    font-family: "Arimo", sans-serif; font-size: 23px; line-height: 1.22;
  }
  .bulk-note {
    position: absolute; left: 62px; top: 413px; width: 520px;
    font-size: 27px; font-weight: 700; letter-spacing: 1.5px; line-height: 1.3;
    color: var(--red); text-transform: uppercase;
  }
  .tyre-visual {
    position: absolute; left: 623px; top: 67px; width: 310px; height: 443px;
    border-radius: 48% / 50%;
    background: radial-gradient(ellipse at 60% 50%, #8e8e8e 0%, #4a4a4a 35%, #161616 65%, #0b0b0b 100%);
  }
  .brand-row {
    position: absolute; left: 40px; right: 40px; top: 542px;
    display: flex; justify-content: space-between;
  }
  .brand-item { display: flex; flex-direction: column; align-items: center; gap: 10px; width: 100px; }
  .brand-item .dot { width: 50px; height: 50px; border-radius: 50%; background: #d9d9d9; }
  .brand-item .label { font-size: 16px; font-weight: 600; color: var(--grey); text-transform: uppercase; letter-spacing: .5px; }
  .contact-bar {
    position: absolute; top: 845px; left: 0; right: 0; height: 48px;
    background: var(--red);
    display: flex; align-items: center; justify-content: space-evenly;
    font-size: 16px; font-weight: 600; letter-spacing: .8px; text-transform: uppercase;
  }
  .contact-item { display: flex; align-items: center; gap: 10px; }
  .contact-item svg { width: 16px; height: 16px; fill: var(--white); }
  .site {
    position: absolute; top: 893px; left: 0; right: 0; height: 67px;
    display: flex; align-items: center; justify-content: center;
    font-size: 24px; font-weight: 700; letter-spacing: 2px; text-transform: uppercase;
  }
</style>
</head>
<body>
<main class="ad">
  <header class="ad-header">
    <span class="brand-mark"></span>
    <span class="brand-name">Tyre Ferns</span>
  </header>

  <section class="ad-body">
    <p class="price-lead">Our tyres <span class="accent">are priced from</span></p>
    <p class="price">KYD<span class="dollar">$</span><span class="amount">55</span><span class="dash">-</span><span class="dollar">$</span><span class="amount">60</span></p>
    <p class="install-note">We offer free installation on tyres when customers come to our facility to get them changed.</p>
    <p class="bulk-note">We sell tyres in bulk and individually.</p>
    <div class="tyre-visual" role="img" aria-label="Product photo of a tyre mounted on a silver alloy wheel"></div>

    <ul class="brand-row" aria-label="Compatible car brands">
      <li class="brand-item"><span class="dot"></span><span class="label">Kelvar</span></li>
      <li class="brand-item"><span class="dot"></span><span class="label">Pratova</span></li>
      <li class="brand-item"><span class="dot"></span><span class="label">Quira</span></li>
      <li class="brand-item"><span class="dot"></span><span class="label">Bexmont</span></li>
      <li class="brand-item"><span class="dot"></span><span class="label">Tavel</span></li>
      <li class="brand-item"><span class="dot"></span><span class="label">Lorimo</span></li>
      <li class="brand-item"><span class="dot"></span><span class="label">Feravi</span></li>
      <li class="brand-item"><span class="dot"></span><span class="label">Drastelmor</span></li>
    </ul>
  </section>

  <footer>
    <div class="contact-bar">
      <span class="contact-item">
        <svg viewBox="0 0 16 16"><path d="M1 3h14v10H1z M1 3l7 6 7-6" fill="none" stroke="#fff" stroke-width="1.6"/></svg>
        info@tyreferns.example
      </span>
      <span class="contact-item">
        <svg viewBox="0 0 16 16"><path d="M4 1l3 3-2 2c1 2 3 4 5 5l2-2 3 3-2 3C7 15 1 9 1 3z"/></svg>
        +1 345 555 0142
      </span>
      <span class="contact-item">
        <svg viewBox="0 0 16 16"><path d="M8 0a5.5 5.5 0 0 0-5.5 5.5C2.5 10 8 16 8 16s5.5-6 5.5-10.5A5.5 5.5 0 0 0 8 0zm0 8a2.5 2.5 0 1 1 0-5 2.5 2.5 0 0 1 0 5z"/></svg>
        41 Marlow Lane, George Town, Cayman Islands
      </span>
    </div>
    <p class="site">tyreferns.example</p>
  </footer>
</main>
</body>
</html>
```